Harborvale LLC
256-738-1054
438 Corwin T. Maddox Blvd.
Marrowfield, AL 35184
harborvalellc97@quillmarsh.com

Heavy& Light Duty Diesel Truck, Trailer, and Equipment Repair
Certified RKT Master Tech & trained techs

Services:
alignments, brakes, suspension, A/C, engine overhauls, DOT inspections, fleet maintenance, computer diagnosis for gas & diesel, warranty work, performance parts for all diesel pickups, Welding & fabrication

Colors, text for Company, phone number, email address in bright red, all other text black.
background color of postcard light grey, black border around pictures.

Industry/Entity Type

Computer

Colors
ec2027

```html
<!DOCTYPE html>
<html lang="en">
<head>
<meta charset="utf-8">
<title>Harborvale LLC Postcard</title>
<link href="https://fonts.googleapis.com/css2?family=Cinzel:wght@700;900&family=Arimo:wght@400;700&display=swap" rel="stylesheet">
<style>
  :root {
    --brand-red: #ec2027;
    --page-bg: #e9e9e9;
    --panel-grey: #a9a9a9;
    --frame-black: #111111;
    --text-white: #ffffff;
    --sky-top: #8d7f93;
    --sky-mid: #c49a9a;
    --road-dark: #1c1318;
  }
  * { box-sizing: border-box; margin: 0; padding: 0; }
  html, body {
    width: 1200px; height: 601px; overflow: hidden;
    background: var(--page-bg);
  }
  .canvas { position: relative; width: 1200px; height: 601px; }

  .card-front {
    position: absolute; left: 131px; top: 120px; width: 467px; height: 360px;
    overflow: hidden;
  }
  .front-photo {
    position: absolute; inset: 0;
    background: linear-gradient(180deg, var(--sky-top) 0%, var(--sky-mid) 38%, #6d4b55 58%, #3a2630 75%, var(--road-dark) 100%);
  }
  .front-shade {
    position: absolute; inset: 0;
    background: linear-gradient(90deg, rgba(0,0,0,0.25) 0%, rgba(0,0,0,0) 60%);
  }
  .brand-name {
    position: absolute; left: 27px; top: 30px;
    font-family: "Cinzel", serif; font-weight: 900; font-size: 30px;
    color: var(--brand-red); letter-spacing: 1px; line-height: 1;
  }
  .contact {
    position: absolute; left: 27px; top: 77px;
    font-family: "Cinzel", serif; font-weight: 700; font-size: 13.5px;
    color: var(--brand-red); line-height: 17.5px;
  }
  .contact .email { font-size: 12.5px; }
  .headline {
    position: absolute; left: 28px; top: 194px;
    font-family: "Arimo", sans-serif; font-weight: 700; font-size: 17.5px;
    color: var(--text-white); text-transform: uppercase; line-height: 19px;
    letter-spacing: 0.6px;
  }
  .services {
    position: absolute; left: 31px; top: 290px; width: 395px;
    font-family: "Arimo", sans-serif; font-size: 8.8px;
    color: var(--text-white); line-height: 10.6px;
  }

  .card-back {
    position: absolute; left: 599px; top: 120px; width: 469px; height: 360px;
    background: var(--panel-grey);
  }
  .photo {
    position: absolute; border: 2px solid var(--frame-black);
  }
  .photo-shop-bay {
    left: 11px; top: 12px; width: 157px; height: 207px;
    background: linear-gradient(180deg, #d8d8d8 0%, #9a9a9a 45%, #3c3c3c 100%);
  }
  .photo-diagnostics {
    left: 168px; top: 12px; width: 290px; height: 207px;
    background: linear-gradient(135deg, #2a2a2a 0%, #8a8a8a 45%, #4a4a4a 100%);
  }
  .photo-shop-exterior {
    left: 11px; top: 219px; width: 447px; height: 129px;
    background: linear-gradient(180deg, #6a6a6a 0%, #cfcfcf 45%, #9c9c9c 75%, #d6d6d6 100%);
  }
</style>
</head>
<body>
<main class="canvas">
  <section class="card-front">
    <div class="front-photo" role="img" aria-label="Semi truck with trailer driving on a highway at sunset"></div>
    <div class="front-shade"></div>
    <h1 class="brand-name">Harborvale LLC</h1>
    <p class="contact">
      256-738-1054 438<br>
      Corwin T. Maddox Blvd.<br>
      Marrowfield, AL 35184<br>
      <span class="email">harborvalellc97@quillmarsh.com</span>
    </p>
    <h2 class="headline">
      Heavy&amp; Light Duty<br>
      Diesel Truck, Trailer,<br>
      and Equipment Repair<br>
      Certified as<br>
      RKT Master Tech &amp; Trained Techs
    </h2>
    <p class="services">
      SERVICES:<br>
      Alignments, brakes, suspension, A/C, engine overhauls, DOT inspections, fleet maintenance, computer diagnosis for gas &amp; diesel, warranty work, performance parts for all diesel pickups, Welding &amp; fabrication
    </p>
  </section>

  <section class="card-back">
    <div class="photo photo-shop-bay" role="img" aria-label="Truck parked inside a repair bay with alignment equipment"></div>
    <div class="photo photo-diagnostics" role="img" aria-label="Technician holding a diagnostic scan tablet in a truck cab"></div>
    <div class="photo photo-shop-exterior" role="img" aria-label="Metal shop building with pickups and a service truck parked in front"></div>
  </section>
</main>
</body>
</html>
```